Business card for Les Brisants-Marins campsite

HORIZONTAL / 85x55
OBJECTIVE
Create a modern, attractive and memorable business card for the Les Brisants-Marins campsite, located on the Île d'Oléron.
The map should make people want to discover the campsite and immediately convey its world: ocean, holidays, nature and conviviality.
VISUAL IDENTITY
The design must be in the same graphic style as our website:
www.lesbrisants-marins.fr
The site is the main reference for the visual atmosphere: colours, typography, shapes, photographs and general universe.
The map and the site must give the impression of belonging to a single brand identity.
A UNIVERSE TO TRANSMIT
• Île d'Oléron
• Atlantic Ocean
• Seaside
• Direct access to the beaches
• Vacation
• Nature
• Family-friendly and welcoming atmosphere
• Relaxation
DESIRED STYLE
Bright, warm, modern, nautical and natural.
We want a creation with a real personality, immediately recognizable, and not a generic camping business card.
FRONT
Prioritize visual impact with:
• Official logo Les Brisants-Marins
• Île d'Oléron
• A strong evocation of the ocean and holidays
• A short and memorable hook
The designer is free to propose their own hook.
BACK
The Marine Breakers
Villages 1 & 2
22 Rue des Vergnes
17310 Saint-Pierre-d'Oléron
France
Tel.: +33 5 46 82 13 47
www.lesbrisants-marins. fr
Possibility of discreet integration:
Direct access to the beaches
Mobile homes • Pitches • Accommodation
Le Varech Bar-Restaurant
FORMAT
Double-sided card: 85 × 55 mm.
Horizontal orientation
AVOID
• Overly institutional design
• Overloaded map
• Generic "camping" style
• Too many pictograms
• Accumulation of texts
• Modification or distortion of the official logo
• Graphic design unrelated to the website
CREATIVE FREEDOM
We are looking for an original proposal.
The designer can play with the graphic codes of the ocean, waves, sun, beach and Île d'Oléron, while remaining faithful to the visual identity of the site.
The card must be aesthetically pleasing and original enough to make people want to keep it.
The objective:
See the map → think about the ocean and holidays → remember Les Brisants-Marins → discover the campsite.
Target Market(s)
All targets
Industry/Entity Type
Tourisme
Contact Information for Business Card
adresse, téléphone, email, site internet + réseaux sociaux
Look and feel
Each slider illustrates characteristics of the customer's brand and the style your logo design should communicate.

```html
<!DOCTYPE html>
<html lang="fr">
<head>
<meta charset="utf-8">
<title>Les Brisants-Marins – carte de visite</title>
<link rel="stylesheet" href="https://fonts.googleapis.com/css2?family=DM+Serif+Display&family=Lexend:wght@400;500;600&family=Oswald:wght@400;500&display=swap">
<style>
  :root{
    --backdrop:#0b2038;
    --navy:#1c2430;
    --ink:#3b3f45;
    --ocean:#2a9fd8;
    --lime:#9cbc22;
    --lagoon:#d2f2fb;
    --white:#ffffff;
  }
  *{box-sizing:border-box;margin:0;padding:0}
  html,body{width:1200px;height:1200px;overflow:hidden}
  body{background:var(--backdrop);font-family:'Lexend',sans-serif;position:relative}

  .card{position:absolute;left:197px;width:806px;height:522px;border-radius:30px;overflow:hidden}
  .card--front{top:56px}
  .card--back{top:610px;background:var(--white)}

  /* front */
  .front-photo{position:absolute;inset:0;
    background:linear-gradient(100deg,#dfe9ee 0%,#a9cfdc 30%,#3f8fbd 58%,#1d5f96 78%,#20639a 100%)}
  .front-photo::after{content:"";position:absolute;left:0;right:0;bottom:0;height:200px;
    background:linear-gradient(180deg,rgba(120,150,90,0) 0%,#7b9a63 45%,#5f7f45 100%)}
  .brand{display:flex;align-items:center;gap:10px;color:var(--ink);
    font-family:'Oswald',sans-serif;font-weight:500;letter-spacing:1px;text-transform:uppercase}
  .brand__dot{border-radius:50%;background:var(--lime);flex:none}
  .brand--front{position:absolute;left:47px;top:96px;font-size:34px}
  .brand--front .brand__dot{width:50px;height:50px}
  .hook-left{position:absolute;left:45px;top:212px;font-family:'DM Serif Display',serif;color:var(--white);text-align:right;width:256px}
  .hook-left__big{display:block;font-size:58px;line-height:1;text-align:left}
  .hook-left__small{display:block;font-size:30px;line-height:1.1}
  .hook-right{position:absolute;right:60px;top:56px;font-family:'DM Serif Display',serif;color:var(--white);text-align:right;font-size:30px;line-height:0.93}
  .hook-right__island{display:block;font-size:80px;line-height:1;margin-top:8px}

  /* back */
  .back-brand{position:absolute;left:70px;width:200px}
  .back-brand .brand{font-size:27px;line-height:1}
  .back-brand .brand__dot{width:38px;height:38px}
  .back-brand__name{display:block}
  .village{display:inline-block;margin:6px 0 0 48px;padding:1px 12px;border-radius:8px;color:var(--white);
    font-size:9px;letter-spacing:2px;text-transform:uppercase}
  .back-brand--one{top:56px}.back-brand--one .village{background:var(--ocean)}
  .back-brand--two{top:172px}.back-brand--two .village{background:var(--lime)}

  .contact{position:absolute;left:314px;display:flex;gap:15px;align-items:flex-start;color:var(--navy);font-size:24px;line-height:30px;font-weight:500;white-space:nowrap}
  .contact__icon{width:32px;height:32px;border-radius:50%;flex:none;display:flex;align-items:center;justify-content:center}
  .contact--phone{top:65px}.contact--phone .contact__icon{background:var(--ocean)}
  .contact--mail{top:111px}.contact--mail .contact__icon{background:#f0e640}
  .contact--address{top:153px}.contact--address .contact__icon{background:var(--lime)}

  .wave{position:absolute;left:0;top:240px;width:806px;height:282px}
  .beaches{position:absolute;left:133px;top:352px;font-family:'DM Serif Display',serif;text-align:right;width:214px}
  .beaches__lead{display:block;color:var(--lime);font-size:25px;line-height:1;white-space:nowrap}
  .beaches__main{display:block;color:var(--ocean);font-size:44px;line-height:1}
  .offer{position:absolute;left:363px;top:358px;list-style:none;font-family:'DM Serif Display',serif;font-size:16px;line-height:21px;color:var(--navy)}
  .offer li::before{content:"★";color:var(--ocean);font-size:11px;margin-right:8px;vertical-align:2px}
  .resto{position:absolute;left:553px;top:301px;width:192px}
  .resto__tag{font-family:'DM Serif Display',serif;font-size:17px;line-height:20px;color:var(--lime)}
  .resto__tag span{color:var(--ocean)}
  .resto__name{margin-top:12px;font-family:'DM Serif Display',serif;font-size:36px;line-height:1;color:var(--navy);text-transform:uppercase;letter-spacing:1px;white-space:nowrap}
  .resto__kind{margin-top:6px;font-size:11px;letter-spacing:3.6px;color:var(--navy);text-transform:uppercase;border-bottom:2px solid var(--ocean);padding-bottom:3px;white-space:nowrap}
  .web{position:absolute;left:82px;top:455px;font-size:21px;font-weight:600;letter-spacing:1px;color:var(--navy)}
  .social{position:absolute;left:471px;top:459px;display:flex;align-items:center;gap:6px;font-size:16px;font-weight:600;color:var(--navy)}
  .social__label{margin-right:4px}
  .social__dot{width:22px;height:22px;border-radius:50%;background:var(--lime)}
</style>
</head>
<body>

<section class="card card--front">
  <div class="front-photo" role="img" aria-label="Vue aérienne du camping au bord de l'océan sur l'île d'Oléron, avec le contour de l'île"></div>
  <div class="brand brand--front"><span class="brand__dot"></span>Les Brisants-Marins</div>
  <p class="hook-left">
    <span class="hook-left__big">L’océan</span>
    <span class="hook-left__small">à vos pieds !</span>
  </p>
  <p class="hook-right">Un séjour les pieds<br>dans l’eau<br>sur l’île
    <span class="hook-right__island">d’Oléron</span>
  </p>
</section>

<section class="card card--back">
  <div class="back-brand back-brand--one">
    <div class="brand"><span class="brand__dot"></span><span class="back-brand__name">Les Brisants-<br>Marins</span></div>
    <span class="village">Village 1</span>
  </div>
  <div class="back-brand back-brand--two">
    <div class="brand"><span class="brand__dot"></span><span class="back-brand__name">Les Brisants-<br>Marins</span></div>
    <span class="village">Village 2</span>
  </div>

  <div class="contact contact--phone">
    <span class="contact__icon"><svg width="18" height="18" viewBox="0 0 24 24"><path fill="#fff" d="M6.6 10.8a15 15 0 0 0 6.6 6.6l2.2-2.2c.3-.3.7-.4 1-.2 1.1.4 2.3.6 3.6.6.6 0 1 .4 1 1V20c0 .6-.4 1-1 1A17 17 0 0 1 3 4c0-.6.4-1 1-1h3.5c.6 0 1 .4 1 1 0 1.3.2 2.5.6 3.6.1.3 0 .7-.2 1z"/></svg></span>
    <span>+33 5 46 82 13 47</span>
  </div>
  <div class="contact contact--mail">
    <span class="contact__icon"><svg width="18" height="14" viewBox="0 0 18 14"><rect x="1" y="1" width="16" height="12" rx="2" fill="none" stroke="#9cbc22" stroke-width="1.6"/><path d="M1.5 2l7.5 6 7.5-6" fill="none" stroke="#9cbc22" stroke-width="1.6"/></svg></span>
    <span>camping@lesbrisants-marins.fr</span>
  </div>
  <div class="contact contact--address">
    <span class="contact__icon"><svg width="16" height="20" viewBox="0 0 16 20"><path fill="#fff" d="M8 0a7 7 0 0 0-7 7c0 5 7 13 7 13s7-8 7-13a7 7 0 0 0-7-7zm0 9.5A2.5 2.5 0 1 1 8 4.5a2.5 2.5 0 0 1 0 5z"/></svg></span>
    <span>22 Rue des Vergnes<br>17310 Saint-Pierre-d'Oléron<br>France</span>
  </div>

  <svg class="wave" viewBox="0 0 806 282" preserveAspectRatio="none" aria-hidden="true">
    <path d="M0 18 C90 70 170 85 250 78 C370 68 500 5 643 10 C720 14 770 40 806 70 L806 282 L0 282 Z" fill="var(--lagoon)"/>
    <path d="M0 18 C90 70 170 85 250 78 C370 68 500 5 643 10 C720 14 770 40 806 70" fill="none" stroke="var(--ocean)" stroke-width="6"/>
  </svg>

  <p class="beaches"><span class="beaches__lead">Accès direct aux</span><span class="beaches__main">Plages</span></p>
  <ul class="offer">
    <li>Mobil-homes</li>
    <li>Emplacements</li>
    <li>Hébergements</li>
  </ul>

  <div class="resto">
    <p class="resto__tag">Un goût de vacances à<br><span>chaque assiette</span></p>
    <p class="resto__name">Le Varech</p>
    <p class="resto__kind">Bar / Restaurant</p>
  </div>

  <p class="web">www.lesbrisants-marins.fr</p>
  <div class="social"><span class="social__label">SUIVEZ-NOUS SUR</span>
    <span class="social__dot"></span><span class="social__dot"></span><span class="social__dot"></span><span class="social__dot"></span>
  </div>
</section>

</body>
</html>
```